Lantern Grid Infographic

We need the 2 pptx mock-ups turned to 2 infographics. please add the logo to the infographics. The colours used on the mock-ups are example colours and can be changed - a gradient scale or the colours used on the mock-up would be great!

```html
<!DOCTYPE html>
<html lang="en">
<head>
<meta charset="UTF-8">
<title>Lantern Grid Infographic</title>
<link rel="stylesheet" href="https://fonts.googleapis.com/css2?family=Montserrat:wght@300;500;600;700;800&display=swap">
<style>
  :root {
    --ink: #111111;
    --ink-soft: #5a5a5a;
    --inner-ink: #2a2a2a;
    --logo-ink: #1b4e8a;
    --paper: #ffffff;

    --plum-dark: #8b1040;
    --plum-mid: #b8296a;
    --plum-light: #e8a1c2;
    --pink-mid: #d6336c;
    --pink-light: #f49ab9;
    --red-dark: #d42038;
    --red-mid: #e0435a;
    --red-light: #f3a0ae;
    --orange-dark: #f47a1a;
    --orange-mid: #d9762c;
    --orange-light: #f5be94;
    --cyan-dark: #27c4d0;
    --cyan-mid: #6ad9e0;
    --cyan-light: #b5eef2;
    --blue-dark: #0e93d6;
    --blue-mid: #3db3dd;
    --blue-light: #a9ddef;
    --navy-dark: #0f4d7a;
    --navy-mid: #2e86b8;
    --navy-light: #96cde9;
  }
  html, body {
    margin: 0;
    padding: 0;
    overflow: hidden;
    background: var(--paper);
  }
  .canvas {
    position: relative;
    width: 1200px;
    height: 1000px;
    overflow: hidden;
    background: var(--paper);
    font-family: "Montserrat", sans-serif;
  }
  .headline {
    position: absolute;
    left: 51px;
    top: 50px;
    margin: 0;
  }
  .headline-title {
    display: block;
    font-weight: 800;
    font-size: 40px;
    line-height: 1;
    color: var(--ink);
    letter-spacing: 0.5px;
  }
  .headline-sub {
    display: block;
    margin-top: 6px;
    font-weight: 300;
    font-size: 36px;
    line-height: 1;
    color: var(--ink-soft);
    letter-spacing: 2px;
  }
  .wheel {
    position: absolute;
    left: 0;
    top: 0;
  }
  .label {
    font-family: "Montserrat", sans-serif;
    text-anchor: middle;
    dominant-baseline: middle;
  }
  .label-outer { font-size: 16px; font-weight: 600; fill: var(--paper); }
  .label-middle { font-size: 15px; font-weight: 600; fill: var(--paper); }
  .label-inner { font-size: 15px; font-weight: 700; fill: var(--inner-ink); }
  .hub { fill: var(--paper); filter: drop-shadow(0 0 6px rgba(0,0,0,0.25)); }
  .hub-name {
    font-family: "Montserrat", sans-serif;
    font-size: 25px;
    font-weight: 700;
    fill: var(--logo-ink);
    text-anchor: middle;
    dominant-baseline: middle;
  }
</style>
</head>
<body>
<div class="canvas">
  <h1 class="headline">
    <span class="headline-title">LANTERN GRID</span>
    <span class="headline-sub">INFOGRAPHIC</span>
  </h1>

  <svg class="wheel" width="1200" height="1000" viewBox="-611 -533 1200 1000" xmlns="http://www.w3.org/2000/svg">
    <defs>
      <path id="wedge-outer" d="M0 0 L0 -400 A400 400 0 0 1 200 -346.41 Z"/>
      <path id="wedge-middle" d="M0 0 L0 -270 A270 270 0 0 1 135 -233.83 Z"/>
      <path id="wedge-inner" d="M0 0 L0 -155 A155 155 0 0 1 77.5 -134.23 Z"/>
    </defs>

    <g class="ring-outer">
      <use href="#wedge-outer" transform="rotate(0)" fill="var(--plum-dark)"/>
      <use href="#wedge-outer" transform="rotate(30)" fill="var(--red-dark)"/>
      <use href="#wedge-outer" transform="rotate(60)" fill="var(--orange-dark)"/>
      <use href="#wedge-outer" transform="rotate(90)" fill="var(--cyan-dark)"/>
      <use href="#wedge-outer" transform="rotate(120)" fill="var(--blue-dark)"/>
      <use href="#wedge-outer" transform="rotate(150)" fill="var(--navy-dark)"/>
      <use href="#wedge-outer" transform="rotate(180)" fill="var(--plum-dark)"/>
      <use href="#wedge-outer" transform="rotate(210)" fill="var(--red-dark)"/>
      <use href="#wedge-outer" transform="rotate(240)" fill="var(--orange-dark)"/>
      <use href="#wedge-outer" transform="rotate(270)" fill="var(--cyan-dark)"/>
      <use href="#wedge-outer" transform="rotate(300)" fill="var(--blue-dark)"/>
      <use href="#wedge-outer" transform="rotate(330)" fill="var(--navy-dark)"/>
    </g>

    <g class="ring-middle">
      <use href="#wedge-middle" transform="rotate(0)" fill="var(--pink-mid)"/>
      <use href="#wedge-middle" transform="rotate(30)" fill="var(--red-mid)"/>
      <use href="#wedge-middle" transform="rotate(60)" fill="var(--orange-mid)"/>
      <use href="#wedge-middle" transform="rotate(90)" fill="var(--cyan-mid)"/>
      <use href="#wedge-middle" transform="rotate(120)" fill="var(--blue-mid)"/>
      <use href="#wedge-middle" transform="rotate(150)" fill="var(--navy-mid)"/>
      <use href="#wedge-middle" transform="rotate(180)" fill="var(--plum-mid)"/>
      <use href="#wedge-middle" transform="rotate(210)" fill="var(--red-mid)"/>
      <use href="#wedge-middle" transform="rotate(240)" fill="var(--orange-mid)"/>
      <use href="#wedge-middle" transform="rotate(270)" fill="var(--cyan-mid)"/>
      <use href="#wedge-middle" transform="rotate(300)" fill="var(--blue-mid)"/>
      <use href="#wedge-middle" transform="rotate(330)" fill="var(--navy-mid)"/>
    </g>

    <g class="ring-inner">
      <use href="#wedge-inner" transform="rotate(0)" fill="var(--pink-light)"/>
      <use href="#wedge-inner" transform="rotate(30)" fill="var(--red-light)"/>
      <use href="#wedge-inner" transform="rotate(60)" fill="var(--orange-light)"/>
      <use href="#wedge-inner" transform="rotate(90)" fill="var(--cyan-light)"/>
      <use href="#wedge-inner" transform="rotate(120)" fill="var(--blue-light)"/>
      <use href="#wedge-inner" transform="rotate(150)" fill="var(--navy-light)"/>
      <use href="#wedge-inner" transform="rotate(180)" fill="var(--plum-light)"/>
      <use href="#wedge-inner" transform="rotate(210)" fill="var(--red-light)"/>
      <use href="#wedge-inner" transform="rotate(240)" fill="var(--orange-light)"/>
      <use href="#wedge-inner" transform="rotate(270)" fill="var(--cyan-light)"/>
      <use href="#wedge-inner" transform="rotate(300)" fill="var(--blue-light)"/>
      <use href="#wedge-inner" transform="rotate(330)" fill="var(--navy-light)"/>
    </g>

    <!-- Outer ring labels -->
    <g class="labels-outer">
      <g transform="rotate(-75) translate(335 0)"><text class="label label-outer"><tspan x="0" dy="-19">Brave</tspan><tspan x="0" dy="19">Empowered</tspan><tspan x="0" dy="19">Fulfilled</tspan></text></g>
      <g transform="rotate(-45) translate(335 0)"><text class="label label-outer"><tspan x="0" dy="-19">Ecstatic</tspan><tspan x="0" dy="19">Elated</tspan><tspan x="0" dy="19">Thrilled</tspan></text></g>
      <g transform="rotate(-15) translate(335 0)"><text class="label label-outer"><tspan x="0" dy="-19">Fascinated</tspan><tspan x="0" dy="19">Invested</tspan><tspan x="0" dy="19">Captivated</tspan></text></g>
      <g transform="rotate(15) translate(335 0)"><text class="label label-outer"><tspan x="0" dy="-19">Positive</tspan><tspan x="0" dy="19">Certain</tspan><tspan x="0" dy="19">Convinced</tspan></text></g>
      <g transform="rotate(45) translate(335 0)"><text class="label label-outer"><tspan x="0" dy="-19">Admiration</tspan><tspan x="0" dy="19">Adoration</tspan><tspan x="0" dy="19">Reverence</tspan></text></g>
      <g transform="rotate(75) translate(335 0)"><text class="label label-outer"><tspan x="0" dy="-19">Tranquil</tspan><tspan x="0" dy="19">Calm</tspan><tspan x="0" dy="19">Satisfied</tspan></text></g>
      <g transform="rotate(105) translate(335 0) rotate(180)"><text class="label label-outer"><tspan x="0" dy="-19">Mortified</tspan><tspan x="0" dy="19">Remorseful</tspan><tspan x="0" dy="19">Regretful</tspan></text></g>
      <g transform="rotate(135) translate(335 0) rotate(180)"><text class="label label-outer"><tspan x="0" dy="-19">Isolated</tspan><tspan x="0" dy="19">Powerless</tspan><tspan x="0" dy="19">Heartbroken</tspan></text></g>
      <g transform="rotate(165) translate(335 0) rotate(180)"><text class="label label-outer"><tspan x="0" dy="-19">Stunned</tspan><tspan x="0" dy="19">Shocked</tspan><tspan x="0" dy="19">Startled</tspan></text></g>
      <g transform="rotate(195) translate(335 0) rotate(180)"><text class="label label-outer"><tspan x="0" dy="-19">Worried</tspan><tspan x="0" dy="19">Frightened</tspan><tspan x="0" dy="19">Terrified</tspan></text></g>
      <g transform="rotate(225) translate(335 0) rotate(180)"><text class="label label-outer"><tspan x="0" dy="-19">Mortified</tspan><tspan x="0" dy="19">Revolted</tspan><tspan x="0" dy="19">Repulsed</tspan></text></g>
      <g transform="rotate(255) translate(335 0) rotate(180)"><text class="label label-outer"><tspan x="0" dy="-19">Aggravated</tspan><tspan x="0" dy="19">Irritated</tspan><tspan x="0" dy="19">Jealous</tspan></text></g>
    </g>

    <!-- Middle ring labels -->
    <g class="labels-middle">
      <g transform="rotate(-75) translate(212 0)"><text class="label label-middle"><tspan x="0" dy="-9">Confident</tspan><tspan x="0" dy="18">Encouraged</tspan></text></g>
      <g transform="rotate(-45) translate(212 0)"><text class="label label-middle"><tspan x="0" dy="-9">Excited</tspan><tspan x="0" dy="18">Happy</tspan></text></g>
      <g transform="rotate(-15) translate(212 0)"><text class="label label-middle"><tspan x="0" dy="-9">Engaged</tspan><tspan x="0" dy="18">Curious</tspan></text></g>
      <g transform="rotate(15) translate(212 0)"><text class="label label-middle"><tspan x="0" dy="-9">Secure</tspan><tspan x="0" dy="18">Optimistic</tspan></text></g>
      <g transform="rotate(45) translate(212 0)"><text class="label label-middle"><tspan x="0" dy="-9">Affectionate</tspan><tspan x="0" dy="18">Connected</tspan></text></g>
      <g transform="rotate(75) translate(212 0)"><text class="label label-middle"><tspan x="0" dy="-9">Relaxed</tspan><tspan x="0" dy="18">Content</tspan></text></g>
      <g transform="rotate(105) translate(212 0) rotate(180)"><text class="label label-middle"><tspan x="0" dy="-9">Embarrassed</tspan><tspan x="0" dy="18">Guilty</tspan></text></g>
      <g transform="rotate(135) translate(212 0) rotate(180)"><text class="label label-middle"><tspan x="0" dy="-9">Lonely</tspan><tspan x="0" dy="18">Disappointed</tspan></text></g>
      <g transform="rotate(165) translate(212 0) rotate(180)"><text class="label label-middle"><tspan x="0" dy="-9">Confused</tspan><tspan x="0" dy="18">Amazed</tspan></text></g>
      <g transform="rotate(195) translate(212 0) rotate(180)"><text class="label label-middle"><tspan x="0" dy="-9">Scared</tspan><tspan x="0" dy="18">Nervous</tspan></text></g>
      <g transform="rotate(225) translate(212 0) rotate(180)"><text class="label label-middle"><tspan x="0" dy="-9">Appalled</tspan><tspan x="0" dy="18">Sickened</tspan></text></g>
      <g transform="rotate(255) translate(212 0) rotate(180)"><text class="label label-middle"><tspan x="0" dy="-9">Frustrated</tspan><tspan x="0" dy="18">Upset</tspan></text></g>
    </g>

    <!-- Inner ring labels -->
    <g class="labels-inner">
      <g transform="rotate(-75) translate(108 0)"><text class="label label-inner">Proud</text></g>
      <g transform="rotate(-45) translate(108 0)"><text class="label label-inner">Joyful</text></g>
      <g transform="rotate(-15) translate(108 0)"><text class="label label-inner">Intrigued</text></g>
      <g transform="rotate(15) translate(108 0)"><text class="label label-inner">Trusting</text></g>
      <g transform="rotate(45) translate(108 0)"><text class="label label-inner">Loving</text></g>
      <g transform="rotate(75) translate(108 0)"><text class="label label-inner">Peaceful</text></g>
      <g transform="rotate(105) translate(108 0) rotate(180)"><text class="label label-inner">Ashamed</text></g>
      <g transform="rotate(135) translate(108 0) rotate(180)"><text class="label label-inner">Sad</text></g>
      <g transform="rotate(165) translate(108 0) rotate(180)"><text class="label label-inner">Surprised</text></g>
      <g transform="rotate(195) translate(108 0) rotate(180)"><text class="label label-inner">Afraid</text></g>
      <g transform="rotate(225) translate(108 0) rotate(180)"><text class="label label-inner">Disgusted</text></g>
      <g transform="rotate(255) translate(108 0) rotate(180)"><text class="label label-inner">Angry</text></g>
    </g>

    <g class="hub-group">
      <circle class="hub" cx="0" cy="0" r="60"/>
      <text class="hub-name"><tspan x="0" dy="-14">Logo</tspan><tspan x="0" dy="28">Here</tspan></text>
    </g>
  </svg>
</div>
</body>
</html>
```